Business Card *

A business card design
Use the logo uploaded in the brief page.
You may use placeholders in your design layouts.
I will provide the actual business card details to the winning designer.

Logo
Place for contact info (name, title, phone, email, etc)

Requirements
Must have
• Logo

```html
<!DOCTYPE html>
<html lang="en">
<head>
<meta charset="utf-8">
<title>Northvale Business Card</title>
<link rel="stylesheet" href="https://fonts.googleapis.com/css2?family=Montserrat:wght@400;700&family=Roboto:wght@300;400&display=swap">
<style>
  :root {
    --bg: #dcdcda;
    --card-white: #ffffff;
    --card-black: #141414;
    --green: #3fb54a;
    --lime: #8cc63f;
    --grey: #8a8a8a;
    --grey-dark: #7a7a7a;
  }
  * { margin: 0; padding: 0; box-sizing: border-box; }
  html, body { width: 1200px; height: 801px; overflow: hidden; }
  body {
    background: var(--bg);
    position: relative;
    font-family: "Roboto", sans-serif;
  }
  .card {
    position: absolute;
    top: 246px;
    width: 540px;
    height: 309px;
    border-bottom: 4px solid var(--green);
    box-shadow: 0 10px 24px rgba(0,0,0,.18);
    overflow: hidden;
  }
  .card-front { left: 40px; background: var(--card-white); }
  .card-back { left: 620px; background: var(--card-black); }

  .brand {
    position: absolute;
    left: 36px;
    top: 0;
    height: 100%;
    width: 230px;
    display: flex;
    align-items: center;
    gap: 10px;
  }
  .brand-dot {
    width: 30px; height: 30px;
    border-radius: 50%;
    background: var(--green);
    flex: none;
  }
  .brand-name {
    font-family: "Montserrat", sans-serif;
    font-weight: 700;
    font-size: 28px;
    letter-spacing: 1px;
    color: var(--grey-dark);
  }
  .divider {
    position: absolute;
    left: 276px;
    top: 64px;
    width: 2px;
    height: 180px;
    background: var(--lime);
  }
  .contact {
    position: absolute;
    left: 298px;
    top: 66px;
    color: var(--grey);
    font-weight: 300;
    font-size: 13px;
    line-height: 19px;
  }
  .contact-name {
    font-family: "Montserrat", sans-serif;
    font-weight: 700;
    font-size: 19px;
    color: var(--green);
    line-height: 24px;
  }
  .contact-title { font-size: 14px; margin-bottom: 8px; }
  .contact-address { margin-bottom: 4px; }
  .contact-row { display: flex; align-items: center; gap: 7px; }
  .contact-row svg { width: 12px; height: 12px; flex: none; }
  .web-accent { color: var(--green); }

  .pattern {
    position: absolute;
    inset: 0;
    background: linear-gradient(125deg, #3a3a3a 0%, #222 40%, #0e0e0e 100%);
  }
  .back-brand {
    position: absolute;
    right: 70px;
    top: 170px;
    display: flex;
    align-items: center;
    gap: 8px;
  }
  .back-brand .brand-dot { width: 20px; height: 20px; }
  .back-brand .brand-name { font-size: 16px; color: var(--green); }
</style>
</head>
<body>
  <section class="card card-front">
    <div class="brand">
      <span class="brand-dot"></span>
      <span class="brand-name">NORTHVALE</span>
    </div>
    <div class="divider"></div>
    <div class="contact">
      <p class="contact-name">OWEN MARSH</p>
      <p class="contact-title">Managing Director</p>
      <p class="contact-address">Alder Park Road,<br>Suite 120 Lakeside</p>
      <p class="contact-row">
        <svg viewBox="0 0 12 12"><path fill="#3fb54a" d="M2.5 1l2 2.2-1 1.3c.7 1.5 1.6 2.4 3 3l1.3-1 2.2 2-1.2 1.5C5 9.5 2.5 7 1 2.2z"/></svg>
        555.201.4870
      </p>
      <p class="contact-row">
        <svg viewBox="0 0 12 12"><rect x="1" y="2.5" width="10" height="7" fill="#3fb54a"/><path d="M1 2.5l5 4 5-4" fill="none" stroke="#fff" stroke-width="1"/></svg>
        owen@northvale.com
      </p>
      <p class="contact-row">
        <svg viewBox="0 0 12 12"><circle cx="6" cy="6" r="5" fill="#3fb54a"/><path d="M1 6h10M6 1c-2 2.5-2 7.5 0 10M6 1c2 2.5 2 7.5 0 10" fill="none" stroke="#fff" stroke-width=".8"/></svg>
        www.<span class="web-accent">northvale.com</span>
      </p>
    </div>
  </section>

  <section class="card card-back">
    <div class="pattern" role="img" aria-label="Repeating embossed gloss pattern of the brand emblem on black"></div>
    <div class="back-brand">
      <span class="brand-dot"></span>
      <span class="brand-name">NORTHVALE</span>
    </div>
  </section>
</body>
</html>
```